Bref créative
logo for mining tool supplier
Durable Quarry Fittings
Professional
Luka Vranek
Manager
42 Tindale ave
Wirrabong NSW 2581
sales@quarry-fittings.com.au
quarry-fittings.com.au

```html
<!DOCTYPE html>
<html lang="en">
<head>
<meta charset="utf-8">
<title>Durable Quarry Fittings – Business Card</title>
<link rel="stylesheet" href="https://fonts.googleapis.com/css2?family=Open+Sans:wght@400;600;700;800&display=swap">
<style>
  :root {
    --card-top: #ffffff;
    --card-fade: #e9e9ea;
    --brand-blue: #2fa3e0;
    --brand-blue-deep: #1b8fd0;
    --brand-orange: #f26b1d;
    --ink-name: #1f3b5a;
    --ink-role: #ffffff;
    --text-light: #ffffff;
  }
  * { margin: 0; padding: 0; box-sizing: border-box; }
  html, body { width: 1200px; height: 770px; overflow: hidden; }
  body { font-family: "Open Sans", Arial, sans-serif; background: var(--card-top); }

  .business-card {
    position: relative;
    width: 1200px;
    height: 770px;
    overflow: hidden;
    background: radial-gradient(ellipse at 55% 25%, var(--card-top) 35%, var(--card-fade) 100%);
  }

  .wave-band { position: absolute; inset: 0; width: 1200px; height: 770px; }

  .brand {
    position: absolute;
    top: 62px;
    left: 0;
    width: 1200px;
    text-align: center;
  }
  .brand-mark {
    display: inline-flex;
    align-items: center;
    gap: 22px;
  }
  .brand-dot {
    width: 62px;
    height: 62px;
    border-radius: 50%;
    background: var(--brand-blue);
  }
  .brand-name {
    font-weight: 800;
    font-size: 104px;
    line-height: 1;
    letter-spacing: 2px;
    color: var(--brand-orange);
  }
  .brand-tagline {
    margin-top: 6px;
    padding-left: 150px;
    font-weight: 700;
    font-size: 31px;
    letter-spacing: 0.5px;
    color: var(--brand-blue-deep);
  }

  .contact-list {
    position: absolute;
    left: 40px;
    top: 478px;
    list-style: none;
    color: var(--text-light);
    font-size: 27px;
    line-height: 42px;
  }
  .contact-list li { display: flex; align-items: center; gap: 12px; }
  .contact-list li.no-icon { padding-left: 40px; }
  .contact-icon { width: 28px; height: 28px; flex: none; }

  .person {
    position: absolute;
    right: 42px;
    top: 618px;
    text-align: right;
  }
  .person-name {
    font-weight: 700;
    font-size: 31px;
    color: var(--ink-name);
  }
  .person-role {
    font-size: 25px;
    color: var(--ink-role);
  }
</style>
</head>
<body>
<div class="business-card">

  <svg class="wave-band" viewBox="0 0 1200 770" aria-hidden="true">
    <path fill="var(--brand-blue)" d="M0,410 C260,395 520,500 760,548 C960,588 1100,520 1200,468 V770 H0 Z"/>
    <path fill="var(--card-top)" d="M300,448 C600,560 920,610 1200,410 L1200,452 C930,640 600,590 300,448 Z"/>
    <path fill="var(--brand-orange)" d="M360,452 C640,560 950,560 1200,340 L1200,392 C960,600 650,600 360,452 Z"/>
    <path fill="var(--brand-orange)" d="M560,548 C780,610 1010,600 1200,470 L1200,488 C1010,628 780,632 560,548 Z"/>
  </svg>

  <header class="brand">
    <div class="brand-mark">
      <span class="brand-dot"></span>
      <span class="brand-name">DQFR</span>
    </div>
    <div class="brand-tagline">DURABLE QUARRY FITTINGS</div>
  </header>

  <ul class="contact-list">
    <li>
      <svg class="contact-icon" viewBox="0 0 28 28"><circle cx="14" cy="14" r="14" fill="#fff"/><path d="M7 14 L14 8 L21 14 V21 H16 V17 H12 V21 H7 Z" fill="var(--brand-blue)"/></svg>
      42 Tindale ave
    </li>
    <li class="no-icon">Wirrabong NSW 2581</li>
    <li>
      <svg class="contact-icon" viewBox="0 0 28 28"><circle cx="14" cy="14" r="14" fill="#fff"/><path d="M10 7 L13 10 L11 13 C12 15 13 16 15 17 L18 15 L21 18 L19 21 C13 20 8 15 7 9 Z" fill="var(--brand-blue)"/></svg>
      0482-517-306
    </li>
    <li>
      <svg class="contact-icon" viewBox="0 0 28 28"><circle cx="14" cy="14" r="14" fill="#fff"/><rect x="7" y="9" width="14" height="10" fill="var(--brand-blue)"/><path d="M7 9 L14 15 L21 9" fill="none" stroke="#fff" stroke-width="1.5"/></svg>
      sales@quarry-fittings.com.au
    </li>
    <li>
      <svg class="contact-icon" viewBox="0 0 28 28"><circle cx="14" cy="14" r="14" fill="#fff"/><g fill="none" stroke="var(--brand-blue)" stroke-width="1.6"><circle cx="14" cy="14" r="7"/><ellipse cx="14" cy="14" rx="3" ry="7"/><line x1="7" y1="14" x2="21" y2="14"/></g></svg>
      www.quarry-fittings.com.au
    </li>
  </ul>

  <div class="person">
    <div class="person-name">Luka Vranek</div>
    <div class="person-role">Manager</div>
  </div>

</div>
</body>
</html>
```